Solarinho 4

Executive Corporate Housing Presentation (B2B Mobility Asset)
We are creating a Corporate Serviced Residence Pitch Deck for international corporate clients (e.g. Velnoria, global mobility teams, relocation departments).
The document is not a traditional real estate brochure. It is a B2B operational housing presentation designed for procurement, HR and corporate mobility decision-makers.
OBJECTIVE
The goal is to communicate:
Operational clarity
Corporate compliance readiness
Location feasibility
Building structure and usability
Executive-level accommodation standard
Reduced relocation and HR friction
DESIGN STYLE
The visual identity should be:
Clean corporate (Harbrook / Corvane / Velnoria style)
Minimalist, high whitespace
Structured and modular (not emotional storytelling)
Data + diagram driven
Subtle luxury (not hospitality marketing)
🚫AVOID
Real estate marketing style
Nestlyo / hospitality visuals
Overly emotional language or lifestyle imagery
Cluttered property listings
Dense technical architectural drawings
KEY VISUAL ELEMENT
Strong emphasis on:
Simplified building diagrams (hotel-style mapping)
Flow-based visuals (how users move through the building)
Corporate icons (access, parking, units, workspace)
Modular information blocks
DESIGN INTENT
The document should feel like:
“A corporate mobility solution presentation”
not
“a luxury property brochure”
Document will be around 12 pages long, I will provide all text and pictures. Enclosed an idea of the desired style. It has to be possible to make changes in the document (PDF - change renders to pictures & change the company's name if needed)
International corporate clients

```html
<!DOCTYPE html>
<html lang="en">
<head>
<meta charset="utf-8">
<title>Solarinho 4 – Executive Corporate Housing</title>
<link href="https://fonts.googleapis.com/css2?family=Montserrat:wght@300;400;500;600;700;800&family=Mulish:wght@400;600&display=swap" rel="stylesheet">
<style>
:root{
  --board:#262626;
  --paper:#ffffff;
  --band:#f6f5f3;
  --ink:#263d4a;
  --text:#4a4f55;
  --gold:#a88a46;
  --beige:#ece3cf;
  --olive:#6f6630;
  --salvia:#6e6a2a;
  --bordo:#7c2b2b;
  --doura:#d3a545;
  --marina:#2f4a5a;
  --terra:#5a4f25;
}
*{margin:0;padding:0;box-sizing:border-box}
html,body{width:1200px;height:898px;overflow:hidden;background:var(--board)}
body{position:relative;font-family:'Montserrat',sans-serif;color:var(--ink)}
.slide{position:absolute;width:521px;height:372px;background:var(--paper);overflow:hidden}
.s1{left:51px;top:53px}.s2{left:619px;top:53px}.s3{left:51px;top:468px}.s4{left:619px;top:468px}
.abs{position:absolute}
svg.layer{position:absolute;left:0;top:0}

/* cover */
.brand{left:29px;top:32px;display:flex;align-items:center;gap:9px;font-weight:500;font-size:11.5px;letter-spacing:1.6px;color:var(--gold)}
.brand-mark{width:22px;height:22px;border:1.2px solid var(--gold)}
.cover-title{left:28px;top:84px;font-weight:800;font-size:30.5px;line-height:35px;letter-spacing:1.6px;color:var(--ink)}
.cover-tag{left:28px;top:196px;font-weight:700;font-size:11.5px;line-height:15px;letter-spacing:.8px;color:var(--gold)}
.cover-body{left:28px;top:240px;font-weight:500;font-size:8.3px;line-height:10.3px;letter-spacing:.3px;color:var(--ink)}
.url{left:29px;top:325px;font-weight:700;font-size:8.3px;letter-spacing:.6px;color:#fff}
.fact{top:294px;width:80px;text-align:center;font-size:7px;letter-spacing:.3px;color:var(--text)}
.fact svg{display:block;margin:0 auto 4px}
.fact b{display:block;font-weight:700;font-size:7px;color:var(--ink)}
.vrule{position:absolute;width:1px;background:#ddd}

/* section headers */
.sec-num{top:31px;left:31px;font-weight:300;font-size:20px;color:var(--gold)}
.sec-title{top:33px;left:66px;font-weight:600;font-size:18.5px;line-height:20px;letter-spacing:.3px;color:var(--ink)}
.sec-sub{top:55px;left:66px;font-weight:300;font-size:12.5px;letter-spacing:.1px;color:var(--ink)}

.item{left:33px;display:flex;gap:14px}
.item svg{flex:none;margin-top:2px}
.item h3{font-weight:500;font-size:9.5px;letter-spacing:.3px;color:var(--ink);margin-bottom:2px}
.item p{font-family:'Mulish',sans-serif;font-size:7px;line-height:8.8px;color:var(--text);padding-left:1px}

.stat{top:324px;width:140px;text-align:center}
.stat b{display:block;font-weight:500;font-size:11px;color:var(--gold)}
.stat span{display:block;font-weight:400;font-size:9px;color:var(--ink);margin-top:1px}

.feat{top:328px;display:flex;gap:6px;align-items:flex-start}
.feat h4{font-weight:500;font-size:7px;letter-spacing:.2px;color:var(--ink)}
.feat p{font-family:'Mulish',sans-serif;font-size:6.2px;color:var(--text);margin-top:1px}

/* design cards */
.card{position:absolute;top:94px;width:84px;height:183px;background:#fff;border:1px solid #ececec;box-shadow:0 1px 4px rgba(0,0,0,.06);text-align:center;font-family:'Mulish',sans-serif;color:#555}
.card-head{height:18px;line-height:18px;font-family:'Montserrat',sans-serif;font-weight:500;font-size:8.5px;letter-spacing:.5px;color:#fff}
.card-photo{height:37px}
.card-cap{height:28px;padding-top:5px;font-size:6.8px;line-height:9.5px;color:#3b3b3b;border-bottom:1px solid #eee;margin:0 8px}
.card-n{font-size:9px;color:var(--ink);margin-top:5px}
.card-l{font-size:6.2px;color:#666;margin-top:1px}
.card-size{font-family:'Montserrat',sans-serif;font-weight:500;font-size:9px;color:var(--gold);margin-top:8px}
</style>
</head>
<body>

<!-- COVER -->
<section class="slide s1">
  <svg class="layer" width="521" height="372" role="img" aria-label="Photo of a modern concrete villa with glass facades beside a reflecting pool">
    <defs>
      <linearGradient id="villa" x1="0" y1="0" x2="0" y2="1">
        <stop offset="0" stop-color="#b9d3e4"/>
        <stop offset=".45" stop-color="#c9c6bd"/>
        <stop offset=".7" stop-color="#6f8a52"/>
        <stop offset="1" stop-color="#2e4a55"/>
      </linearGradient>
    </defs>
    <polygon points="330,0 521,0 521,252 215,252 166,341 150,341" fill="url(#villa)"/>
  </svg>
  <svg class="layer" width="521" height="372" aria-hidden="true">
    <polygon points="301,0 314,0 269,71 256,71" fill="var(--beige)"/>
    <polygon points="320,0 333,0 266,114 253,114" fill="var(--gold)"/>
    <polygon points="0,322 140,322 130,339 0,339" fill="var(--olive)"/>
    <polygon points="143,322 151,322 141,339 133,339" fill="var(--beige)"/>
  </svg>
  <div class="abs brand"><span class="brand-mark"></span>SOLARINHO 4</div>
  <h1 class="abs cover-title">EXECUTIVE<br>CORPORATE<br>HOUSING</h1>
  <p class="abs cover-tag">MOVE-IN READY COMFORT.<br>EFFORTLESS LIVING.</p>
  <p class="abs cover-body">Lorem Ipsum is simply dummy<br>text of the printing and<br>typesetting industry,</p>
  <div class="abs url">SOLARINHO4.COM</div>

  <div class="abs fact" style="left:192px">
    <svg width="28" height="28" viewBox="0 0 28 28" fill="none" stroke="#6a6a6a" stroke-width="1"><rect x="6" y="3" width="16" height="23"/><path d="M9 7h3M16 7h3M9 11h3M16 11h3M9 15h3M16 15h3M9 19h3M16 19h3M12 26v-4h4v4"/></svg>
    <b>1908</b>Restored Building
  </div>
  <div class="vrule" style="left:277px;top:295px;height:44px"></div>
  <div class="abs fact" style="left:275px">
    <svg width="28" height="28" viewBox="0 0 28 28" fill="none" stroke="#6a6a6a" stroke-width="1"><rect x="4" y="6" width="20" height="18"/><path d="M4 12h20M10 6v18M16 18h5M16 15h5"/><circle cx="21" cy="5" r="2.5"/></svg>
    <b>5</b>Unique Designs
  </div>
  <div class="vrule" style="left:359px;top:295px;height:44px"></div>
  <div class="abs fact" style="left:357px">
    <svg width="28" height="28" viewBox="0 0 28 28" fill="none" stroke="#6a6a6a" stroke-width="1"><rect x="4" y="3" width="20" height="23"/><path d="M4 11h9v-8M13 17h11M9 17v9M17 6h4v4h-4z"/></svg>
    <b>85-95 m²</b>Per Apartment
  </div>
  <div class="vrule" style="left:440px;top:295px;height:44px"></div>
  <div class="abs fact" style="left:440px">
    <svg width="28" height="28" viewBox="0 0 28 28" fill="none" stroke="#6a6a6a" stroke-width="1"><rect x="5" y="5" width="16" height="20" rx="1"/><path d="M9 10h8M9 14h8M9 18h4"/><circle cx="21" cy="20" r="4.5"/><path d="M19 20l1.5 1.5 3-3"/></svg>
    <b>Built for</b>Professionals
  </div>
</section>

<!-- LOCATION -->
<section class="slide s2">
  <div class="abs sec-num">01</div>
  <h2 class="abs sec-title">PRIME LOCATION</h2>
  <div class="abs sec-sub">CONNECTED TO EVERYTHING</div>
  <svg class="layer" width="521" height="372" aria-hidden="true">
    <polygon points="297,37 310,37 292,68 279,68" fill="var(--beige)"/>
    <polygon points="315,37 332,37 314,68 297,68" fill="var(--gold)"/>
    <polygon points="0,345 25,306 521,306 521,312 29,312 0,356" fill="var(--olive)"/>
    <polygon points="0,356 29,312 521,312 521,372 0,372" fill="var(--band)"/>
    <line x1="182" y1="321" x2="182" y2="356" stroke="#bbb"/>
    <line x1="354" y1="321" x2="354" y2="356" stroke="#bbb"/>
  </svg>

  <div class="abs item" style="top:95px">
    <svg width="22" height="24" viewBox="0 0 22 24" fill="none" stroke="var(--gold)" stroke-width="1.2"><path d="M11 23s-8-8-8-13a8 8 0 0 1 16 0c0 5-8 13-8 13z"/><circle cx="11" cy="10" r="3"/></svg>
    <div><h3>CENTRAL LISBON</h3><p>Lorem Ipsum is simply dummy<br>text of the printing dsmr.</p></div>
  </div>
  <div class="abs item" style="top:143px">
    <svg width="22" height="24" viewBox="0 0 22 24" fill="none" stroke="var(--gold)" stroke-width="1.2"><path d="M2 15l18-8M8 12l-3-5M12 10l2 8M3 19h8"/></svg>
    <div><h3>TRAVEL ACCESS</h3><p>Lorem Ipsum is simply dummy<br>text of the printing dsmr.</p></div>
  </div>
  <div class="abs item" style="top:192px">
    <svg width="22" height="24" viewBox="0 0 22 24" fill="none" stroke="var(--gold)" stroke-width="1.2"><rect x="1" y="7" width="20" height="14" rx="1"/><path d="M7 7V4h8v3M1 12h20M10 12v3h2v-3"/></svg>
    <div><h3>BUSINESS ACCESS</h3><p>Lorem Ipsum is simply dummy<br>text of the printing dsmr.</p></div>
  </div>
  <div class="abs item" style="top:240px">
    <svg width="22" height="24" viewBox="0 0 22 24" fill="none" stroke="var(--gold)" stroke-width="1.2"><path d="M11 2l8 3v7c0 5-4 9-8 10-4-1-8-5-8-10V5z"/><circle cx="16" cy="18" r="3.5"/><path d="M14.5 18l1 1 2-2"/></svg>
    <div><h3>LIFESTYLE ACCESS</h3><p>Lorem Ipsum is simply dummy<br>text of the printing dsmr.</p></div>
  </div>

  <svg class="abs" style="left:192px;top:143px" width="301" height="125" role="img" aria-label="Dotted world map with coloured location pins">
    <defs><radialGradient id="map" cx=".5" cy=".5" r=".6"><stop offset="0" stop-color="#bcc2c8"/><stop offset="1" stop-color="#eef0f2"/></radialGradient></defs>
    <rect width="301" height="125" rx="40" fill="url(#map)"/>
  </svg>

  <div class="abs stat" style="left:24px"><b>5 MIN</b><span>Metro Access</span></div>
  <div class="abs stat" style="left:198px"><b>10 MIN</b><span>Airport</span></div>
  <div class="abs stat" style="left:366px"><b>10 MIN</b><span>City Center</span></div>
</section>

<!-- BUILDING -->
<section class="slide s3">
  <div class="abs sec-num">02</div>
  <h2 class="abs sec-title">THE BUILDING</h2>
  <div class="abs sec-sub" style="left:68px">STRUCTURE &amp; ACCESS</div>

  <svg class="abs" style="left:286px;top:31px" width="206" height="250" role="img" aria-label="Exploded line drawing of the building showing roof, upper floor and ground floor">
    <defs><linearGradient id="diagram" x1="0" y1="0" x2="0" y2="1"><stop offset="0" stop-color="#f2f2f2"/><stop offset="1" stop-color="#fafafa"/></linearGradient></defs>
    <rect width="206" height="250" fill="url(#diagram)"/>
  </svg>

  <svg class="layer" width="523" height="372" aria-hidden="true">
    <polygon points="249,37 262,37 244,68 231,68" fill="var(--beige)"/>
    <polygon points="267,37 284,37 266,68 249,68" fill="var(--gold)"/>
    <polygon points="0,345 25,305 523,305 523,311 29,311 0,356" fill="var(--olive)"/>
    <polygon points="0,356 29,311 523,311 523,372 0,372" fill="var(--band)"/>
  </svg>

  <div class="abs item" style="top:95px">
    <svg width="24" height="24" viewBox="0 0 24 24" fill="none" stroke="#6a6a6a" stroke-width="1"><path d="M2 23V2h20v21M2 8h20"/><circle cx="12" cy="17" r="2"/></svg>
    <div><h3>GROUND FLOOR</h3><p>Lorem Ipsum is simply dummy<br>text of the printing dsmr.</p></div>
  </div>
  <div class="abs item" style="top:143px">
    <svg width="24" height="24" viewBox="0 0 24 24" fill="none" stroke="#6a6a6a" stroke-width="1"><rect x="1" y="4" width="22" height="18"/><path d="M1 10h22M5 4v6M9 4v6M13 4v6M17 4v6M10 14h9v6h-9z"/></svg>
    <div><h3>FIRST FLOOR</h3><p>Lorem Ipsum is simply dummy<br>text of the printing dsmr.</p></div>
  </div>
  <div class="abs item" style="top:192px">
    <svg width="24" height="24" viewBox="0 0 24 24" fill="none" stroke="#6a6a6a" stroke-width="1"><path d="M1 6V1h5M18 1h5v5M1 18v5h5M18 23h5v-5M7 19v-7l7-5 5 4v8z"/></svg>
    <div><h3>GARDEN LEVEL</h3><p>Lorem Ipsum is simply dummy<br>text of the printing dsmr.</p></div>
  </div>
  <div class="abs item" style="top:240px">
    <svg width="24" height="24" viewBox="0 0 24 24" fill="none" stroke="#6a6a6a" stroke-width="1"><rect x="2" y="9" width="20" height="14"/><path d="M2 13h20M8 9V3h8v6M8 17h8v6"/></svg>
    <div><h3>ROOFTOP</h3><p>Lorem Ipsum is simply dummy<br>text of the printing dsmr.</p></div>
  </div>

  <div class="abs feat" style="left:64px">
    <svg width="13" height="15" viewBox="0 0 13 15" fill="none" stroke="var(--olive)" stroke-width="1"><path d="M6.5 1l5.5 2v5c0 3-3 5.5-5.5 6.5C4 13.5 1 11 1 8V3z"/><path d="M4 7.5l2 2 3-3.5"/></svg>
    <div><h4>SECURE ACCESS</h4><p>Controlled entry</p></div>
  </div>
  <div class="abs feat" style="left:176px">
    <svg width="13" height="15" viewBox="0 0 13 15" fill="none" stroke="var(--olive)" stroke-width="1"><path d="M6.5 1l5.5 2v5c0 3-3 5.5-5.5 6.5C4 13.5 1 11 1 8V3z"/><path d="M4 7.5l2 2 3-3.5"/></svg>
    <div><h4>ELEVATOR ACCESS</h4><p>All Levels</p></div>
  </div>
  <div class="abs feat" style="left:295px">
    <svg width="13" height="15" viewBox="0 0 13 15" fill="none" stroke="var(--olive)" stroke-width="1"><path d="M6.5 1l5.5 2v5c0 3-3 5.5-5.5 6.5C4 13.5 1 11 1 8V3z"/><path d="M4 7.5l2 2 3-3.5"/></svg>
    <div><h4>SMART BUILDING</h4><p>All Levels</p></div>
  </div>
  <div class="abs feat" style="left:410px">
    <svg width="13" height="15" viewBox="0 0 13 15" fill="none" stroke="var(--olive)" stroke-width="1"><path d="M6.5 1l5.5 2v5c0 3-3 5.5-5.5 6.5C4 13.5 1 11 1 8V3z"/><path d="M4 7.5l2 2 3-3.5"/></svg>
    <div><h4>PRIVATE PARKING</h4><p>On-Site</p></div>
  </div>
</section>

<!-- DESIGNS -->
<section class="slide s4">
  <div class="abs sec-num">03</div>
  <h2 class="abs sec-title">FIVE UNIQUE DESIGNS</h2>
  <div class="abs sec-sub">BUILD FOR CORPORATE LIVING</div>
  <svg class="layer" width="522" height="372" aria-hidden="true">
    <polygon points="312,37 325,37 307,68 294,68" fill="var(--beige)"/>
    <polygon points="330,37 347,37 329,68 312,68" fill="var(--gold)"/>
    <polygon points="0,345 25,306 522,306 522,312 29,312 0,356" fill="var(--olive)"/>
    <polygon points="0,356 29,312 522,312 522,372 0,372" fill="var(--band)"/>
  </svg>

  <div class="card" style="left:30px">
    <div class="card-head" style="background:var(--salvia)">SALVIA</div>
    <div class="card-photo" role="img" aria-label="Olive green dining and living interior" style="background:linear-gradient(180deg,#cfcab4,#8b7d5e)"></div>
    <div class="card-cap">Olive green<br>signature design</div>
    <div class="card-n">2</div><div class="card-l">Bedrooms</div>
    <div class="card-n">2</div><div class="card-l">Bathrooms</div>
    <div class="card-size">85–95 m²</div><div class="card-l">Size Range</div>
  </div>
  <div class="card" style="left:124px">
    <div class="card-head" style="background:var(--bordo)">BORDO</div>
    <div class="card-photo" role="img" aria-label="Warm earthy living room interior" style="background:linear-gradient(180deg,#d9c9b6,#9a7d63)"></div>
    <div class="card-cap">Warm &amp; earthy<br>elegance</div>
    <div class="card-n">2</div><div class="card-l">Bedrooms</div>
    <div class="card-n">2</div><div class="card-l">Bathrooms</div>
    <div class="card-size">85–95 m²</div><div class="card-l">Size Range</div>
  </div>
  <div class="card" style="left:220px">
    <div class="card-head" style="background:var(--doura)">DOURA</div>
    <div class="card-photo" role="img" aria-label="Bright golden-toned living room interior" style="background:linear-gradient(180deg,#e6ddcc,#b59a72)"></div>
    <div class="card-cap">Golden light<br>sophistication</div>
    <div class="card-n">2</div><div class="card-l">Bedrooms</div>
    <div class="card-n">2</div><div class="card-l">Bathrooms</div>
    <div class="card-size">85–95 m²</div><div class="card-l">Size Range</div>
  </div>
  <div class="card" style="left:317px">
    <div class="card-head" style="background:var(--marina)">MARINA</div>
    <div class="card-photo" role="img" aria-label="Living room with blue accent wall" style="background:linear-gradient(90deg,#e5e4df,#3f6b82 70%,#d9d6cf)"></div>
    <div class="card-cap">Mediterranean blue<br>serenity</div>
    <div class="card-n">2</div><div class="card-l">Bedrooms</div>
    <div class="card-n">2</div><div class="card-l">Bathrooms</div>
    <div class="card-size">85–95 m²</div><div class="card-l">Size Range</div>
  </div>
  <div class="card" style="left:413px">
    <div class="card-head" style="background:var(--terra)">TERRA</div>
    <div class="card-photo" role="img" aria-label="Dining area opening onto a garden" style="background:linear-gradient(90deg,#e4e0d8,#a99479 55%,#8fae72)"></div>
    <div class="card-cap">Accessible<br>garden living</div>
    <div class="card-n">2</div><div class="card-l">Bedrooms</div>
    <div class="card-n">2</div><div class="card-l">Bathrooms</div>
    <div class="card-size">85–95 m²</div><div class="card-l">Size Range</div>
    <div class="card-l" style="color:#3b3b3b">Wheelchair accessible</div>
  </div>

  <div class="abs feat" style="left:36px">
    <svg width="17" height="12" viewBox="0 0 17 12" fill="none" stroke="#777" stroke-width="1"><path d="M1 11V4h15v7M3 4V2h11v2M1 8h15"/></svg>
    <div><h4>FULLY FURNISHED</h4><p>Premium design</p></div>
  </div>
  <div class="abs feat" style="left:140px">
    <svg width="14" height="14" viewBox="0 0 14 14" fill="none" stroke="#777" stroke-width="1"><path d="M1 13V6l6-4 6 4v7zM4 13V9h3v4M9 8h2v2H9z"/></svg>
    <div><h4>FULLY EQUIPPED KITCHEN</h4><p>Move-in ready</p></div>
  </div>
  <div class="abs feat" style="left:273px">
    <svg width="14" height="15" viewBox="0 0 14 15" fill="none" stroke="#777" stroke-width="1"><rect x="1" y="1" width="12" height="13" rx="1"/><path d="M1 4h12"/><circle cx="7" cy="9" r="3"/></svg>
    <div><h4>WASHING MACHINE</h4><p>In-Unit</p></div>
  </div>
  <div class="abs feat" style="left:385px">
    <svg width="14" height="14" viewBox="0 0 14 14" fill="none" stroke="#777" stroke-width="1"><path d="M2 5a7 7 0 0 1 10 0M4 7a4 4 0 0 1 6 0"/><circle cx="7" cy="9" r=".8"/><rect x="1" y="10.5" width="12" height="3"/></svg>
    <div><h4>HIGH-SPEED INTERNET</h4><p>Included</p></div>
  </div>
</section>

</body>
</html>
```